Restaurant menu design

I need a menu for a restaurant in Spain.
It has to be bohemian but modern. We need something romantic and elegant.
The restaurant is elegant with good food and an excellent reputation. It is also modern at the same time.
The restaurant is superbly decorated and very chick so we need something "class" to fit in with the surroundings.
The size of the document must be 325 mm in high and 245 mm as a maximum and preferably made in indesign.

Reason: Thank you all for your designs.
So far all your designs are ok but it isn´t what we are looking for. Most of the designs are too loaded, too many colors and too much decoration.

Target Market(s)

Adults of various age groups and different nationalities mostly European.

Industry/Entity Type

Restaurant

Requirements
Must have
• The menu must have two interior pages with the text as in the document attached.It must be easily legible.
Nice to have
• See what kind of menus they use in important restaurants in places like Paris, see what designs are in trend, but Not necessarily doing the same style if it doesn’t fit in with the description above.
Should not have
• Nothing old fashioned.

```html
<!DOCTYPE html>
<html lang="es">
<head>
<meta charset="utf-8">
<title>La Rêverie — Carta</title>
<link rel="stylesheet" href="https://fonts.googleapis.com/css2?family=Caveat&family=EB+Garamond:ital,wght@0,400;1,400&display=swap">
<style>
  :root {
    --plum: #9b4c86;
    --blush: #ead3e0;
    --blush-deep: #dcb8cd;
    --ink: #1c1c1c;
    --rule: #c9c9c9;
    --paper: #ffffff;
  }
  * { margin: 0; padding: 0; box-sizing: border-box; }
  html, body { width: 1200px; height: 796px; overflow: hidden; background: var(--paper); }
  .menu {
    position: relative; width: 1200px; height: 796px;
    background: var(--paper); border: 1px solid var(--rule);
    font-family: "EB Garamond", Georgia, serif; color: var(--ink);
  }
  .side-band {
    position: absolute; left: 0; top: 0; width: 105px; height: 100%;
    background: var(--blush);
  }
  .band-accent {
    position: absolute; left: 0; top: 0; width: 105px; height: 210px;
    background: linear-gradient(180deg, var(--blush-deep) 0%, var(--blush) 100%);
  }
  .brand {
    position: absolute; left: 0; width: 105px; top: 712px;
    display: flex; align-items: center; justify-content: center; gap: 5px;
    color: var(--plum); font-size: 19px; font-family: "EB Garamond", Georgia, serif;
  }
  .brand-dot { width: 7px; height: 7px; border-radius: 50%; background: var(--plum); }
  .page-fold { position: absolute; left: 600px; top: 0; width: 1px; height: 100%; background: #dedede; }
  .section { position: absolute; text-align: center; }
  .section.left { left: 105px; width: 495px; }
  .section.right { left: 601px; width: 599px; }
  .section-title {
    font-family: "Caveat", cursive; font-weight: 400; color: var(--plum);
    font-size: 36px; line-height: 36px; margin-bottom: 14px;
  }
  .section.top .section-title { margin-bottom: 19px; }
  .dish-list { list-style: none; }
  .dish { font-style: italic; font-size: 13.6px; line-height: 17.3px; white-space: nowrap; }
  .right .dish { line-height: 19px; }
  .price { font-size: 9.5px; margin-left: 16px; }
  .sauces {
    position: absolute; left: 670px; top: 377px; width: 459px; height: 36px;
    border: 1px solid #9a9a9a; display: flex; align-items: center; justify-content: center; gap: 8px;
    font-style: italic; font-size: 9.5px; white-space: nowrap;
  }
  .sauces-label { font-family: "Caveat", cursive; color: var(--plum); font-size: 16px; font-style: normal; }
  .sauces .price { font-size: 7.5px; margin-left: 8px; }
</style>
</head>
<body>
<main class="menu">
  <aside class="side-band">
    <div class="band-accent" role="img" aria-label="Decorative pattern area in plum and blush tones"></div>
    <div class="brand"><span class="brand-dot"></span><span>la rêverie</span></div>
  </aside>
  <div class="page-fold"></div>

  <section class="section left top" style="top:55px">
    <h2 class="section-title">Entradas</h2>
    <ul class="dish-list">
      <li class="dish">Ensalada La Rêverie. Lechuga, tomate.<span class="price">7,75 €</span></li>
      <li class="dish">Ensalada Caprese (Tomate y Mozzarella).<span class="price">7,75 €</span></li>
      <li class="dish">Escarola al Queso de Cabra con Bacon.<span class="price">6,75 €</span></li>
      <li class="dish">Cocktail de Gambas, Langostinos y Aguacate.<span class="price">7,50 €</span></li>
      <li class="dish">La Sopa de Pescado.<span class="price">8,25 €</span></li>
      <li class="dish">Crema de Espárragos Trigueros y Calabacín.<span class="price">5,95 €</span></li>
      <li class="dish">Carpaccio de Ternera.<span class="price">11,50 €</span></li>
      <li class="dish">Carpaccio de Salmón al Eneldo.<span class="price">9,75 €</span></li>
      <li class="dish">Carpaccio de Atún.<span class="price">13,95 €</span></li>
      <li class="dish">Melón con Jamón Ibérico.<span class="price">9,25 €</span></li>
      <li class="dish">Parrillada de Verduras.<span class="price">7,95 €</span></li>
      <li class="dish">Parrillada de Verduras Gratinada al Queso de Cabra.<span class="price">8,95 €</span></li>
      <li class="dish">Gambas Roja de la Bahía.<span class="price">12,95 €</span></li>
    </ul>
  </section>

  <section class="section left" style="top:417px">
    <h2 class="section-title">Pescados al Grill</h2>
    <ul class="dish-list">
      <li class="dish">Lubina al Hinojo.<span class="price">15,50 €</span></li>
      <li class="dish">Lubina Fileteada y su Salsa Rústica con Berenjena.<span class="price">18,50 €</span></li>
      <li class="dish">Filete de Rodaballo y su Salsa de Marisco.<span class="price">17,25 €</span></li>
      <li class="dish">Dorada del Mediterráneo.<span class="price">13,95 €</span></li>
      <li class="dish">Lenguado al Grill con Hierbas Provenzales.<span class="price">20,75 €</span></li>
      <li class="dish">Pieza de Atún Fresco y su Salsa Griega.<span class="price">18,95 €</span></li>
      <li class="dish">Lomo de Salmón con Salsa de Frambuesa.<span class="price">11,25 €</span></li>
      <li class="dish">Parrillada de Pescado y Marisco.<span class="price">23,505 €</span></li>
    </ul>
  </section>

  <section class="section left" style="top:659px">
    <h2 class="section-title">Especial Niños</h2>
    <ul class="dish-list">
      <li class="dish">Solomillo Junior, huevo y patatas fritas.<span class="price">6,25 €</span></li>
      <li class="dish">Fish &amp; chips.<span class="price">6,25 €</span></li>
    </ul>
  </section>

  <section class="section right top" style="top:55px">
    <h2 class="section-title">Carnes</h2>
    <ul class="dish-list">
      <li class="dish">Pechuga de Pollo “Madame Lise” con Champiñones y Bacon.<span class="price">11,95 €</span></li>
      <li class="dish">Chuletas de Cordero.<span class="price">14,50 €</span></li>
      <li class="dish">Costillas de Cerdo con Salsa Barbacoa.<span class="price">9,95 €</span></li>
      <li class="dish">Paletilla de Cordero Lechal.<span class="price">19,75 €</span></li>
      <li class="dish">Le Strogonoff. Finas tiras de Solomillo con su Salsa de Champiñones.<span class="price">15,90 €</span></li>
      <li class="dish">Solomillo de Ternera.<span class="price">18,50 €</span></li>
      <li class="dish">Solomillo de Ternera a la Ibérica con Jamón Ibérico y Ligera Salsa de Vino Tinto.<span class="price">20,75 €</span></li>
      <li class="dish">“Hamburger Maison Steak Hachè”. Picata de Solomillo de Ternera, Huevo Frito y Patatas Fritas<span class="price">14,50 €</span></li>
      <li class="dish">Solomillo de Cerdo al Horno con Bacon y su Salsa de Setas.<span class="price">14,25 €</span></li>
      <li class="dish">Entrecôte de Ternera.<span class="price">14,75 €</span></li>
      <li class="dish">T-Bone Steak de Ternera.<span class="price">16,75 €</span></li>
      <li class="dish">Chuletón de Ternera.<span class="price">20,25 €</span></li>
      <li class="dish">Parrillada de Carnes y Embutidos.<span class="price">21,50 €</span></li>
    </ul>
  </section>

  <div class="sauces">
    <span class="sauces-label">Salsas:</span>
    <span>Pimienta.<span class="price">2,85 €</span></span><span>·</span>
    <span>Roquefort.<span class="price">2,95 €</span></span><span>·</span>
    <span>Bearnaise.<span class="price">2,95 €</span></span><span>·</span>
    <span>de Champiñones.<span class="price">2,65 €</span></span>
  </div>

  <section class="section right" style="top:507px">
    <h2 class="section-title">Los Postres de la Rêverie</h2>
    <ul class="dish-list">
      <li class="dish">Frambuesas “La Rêverie”.<span class="price">6,25 €</span></li>
      <li class="dish">Cocktail de Frutas Exóticas.<span class="price">5,25 €</span></li>
      <li class="dish">Sorbete de Limón, Coulis de Fresa y Vodka.<span class="price">5,50 €</span></li>
      <li class="dish">Pastel de Chocolate Casero con su Salsa de Vainilla.<span class="price">6,25 €</span></li>
      <li class="dish">Crême Brulée.<span class="price">6,25 €</span></li>
      <li class="dish">Tarta de Manzana Casera “Tatín” y su Helado de Vainilla.<span class="price">6,95 €</span></li>
      <li class="dish">Copa Glacière.<span class="price">6,75 €</span></li>
      <li class="dish">Pera al Chocolate Caliente y Helado de Macadamia.<span class="price">5,95 €</span></li>
      <li class="dish">Tarta de Queso con Coulis de Fresa.<span class="price">5,75 €</span></li>
      <li class="dish">Nuestra Mousse de Chocolate.<span class="price">5,75 €</span></li>
    </ul>
  </section>
</main>
</body>
</html>
```